BRD business cards Dr. Martin Velk

I need a business card designed for our dental office. We are a "general dental" practice.
Looking for a clean, professional but not too fancy design with our logo and contact information required.
front of card is information/standard business card, backside is appt reminder with lines for date and time of appt
doctors name: Dr. Martin Velk DMD
office name: Velk Family Dental
address: 4827 E Tolland Ave Larkin Shores, FL 34990
phone: 727-555-0173
Dentistry
Office name, Doctor name, address, phone number...etc
- White/off white base color, blue and or black lettering

```html
<!DOCTYPE html>
<html lang="en">
<head>
<meta charset="utf-8">
<title>Velk Family Dental – Business Card</title>
<link href="https://fonts.googleapis.com/css2?family=Cinzel:wght@500;600&family=Arimo:wght@400&display=swap" rel="stylesheet">
<style>
  :root {
    --page-bg: #dcdcdc;
    --card-bg: #f6f4df;
    --ink: #141414;
    --rule: #2a2a2a;
  }
  * { box-sizing: border-box; margin: 0; padding: 0; }
  html, body { width: 1200px; height: 800px; overflow: hidden; }
  body {
    background: var(--page-bg);
    display: flex;
    align-items: center;
    justify-content: center;
    gap: 40px;
    font-family: "Arimo", Arial, sans-serif;
    color: var(--ink);
  }
  .card {
    width: 540px;
    height: 309px;
    background: var(--card-bg);
    border-radius: 22px;
    position: relative;
    display: flex;
    flex-direction: column;
    align-items: center;
  }

  /* Front */
  .card--front { justify-content: center; }
  .brand-name {
    font-family: "Cinzel", "Times New Roman", serif;
    font-weight: 600;
    font-size: 26px;
    letter-spacing: 1px;
    margin-bottom: 14px;
  }
  .doctor-name {
    font-family: "Cinzel", "Times New Roman", serif;
    font-weight: 500;
    font-size: 19px;
    letter-spacing: 1px;
    margin-bottom: 16px;
  }
  .details {
    display: flex;
    align-items: stretch;
    font-size: 14px;
    line-height: 1.45;
  }
  .details__address { text-align: right; padding-right: 12px; font-style: normal; }
  .details__divider { width: 1px; background: var(--rule); }
  .details__contact { padding-left: 12px; list-style: none; }
  .details__contact li { display: flex; align-items: center; gap: 7px; }
  .details__contact svg { width: 11px; height: 11px; flex: none; fill: var(--ink); }

  /* Back */
  .card--back { padding: 34px 40px 0; }
  .back-brand {
    font-family: "Cinzel", "Times New Roman", serif;
    font-weight: 600;
    font-size: 26px;
    letter-spacing: 1px;
    margin-bottom: 36px;
  }
  .form { width: 100%; font-size: 17px; }
  .form__row { display: flex; align-items: baseline; margin-bottom: 22px; }
  .form__label { white-space: nowrap; }
  .form__dots {
    flex: 1;
    border-bottom: 2px dotted var(--ink);
    margin: 0 4px;
    transform: translateY(-3px);
  }
  .form__suffix { font-size: 13px; }
  .notice { font-size: 12.5px; text-align: center; margin-top: 6px; }
</style>
</head>
<body>
  <section class="card card--front" aria-label="Business card front">
    <div class="brand-name">Velk Family Dental</div>
    <h1 class="doctor-name">Dr. Martin Velk DMD</h1>
    <div class="details">
      <address class="details__address">
        Velk Family Dental<br>
        4827 E Tolland Ave<br>
        Larkin Shores, FL 34990
      </address>
      <div class="details__divider"></div>
      <ul class="details__contact">
        <li>
          <svg viewBox="0 0 24 24" aria-hidden="true"><path d="M6.6 10.8c1.4 2.8 3.8 5.1 6.6 6.6l2.2-2.2c.3-.3.7-.4 1-.2 1.1.4 2.3.6 3.6.6.6 0 1 .4 1 1V20c0 .6-.4 1-1 1C10.6 21 3 13.4 3 4c0-.6.4-1 1-1h3.5c.6 0 1 .4 1 1 0 1.3.2 2.5.6 3.6.1.3 0 .7-.2 1z"/></svg>
          727-555-0173
        </li>
        <li>
          <svg viewBox="0 0 24 24" aria-hidden="true"><path d="M2 5h20v14H2z M2 5l10 8 10-8" stroke="#f6f4df" stroke-width="1.6"/></svg>
          info@velkfamilydental.com
        </li>
        <li>
          <svg viewBox="0 0 24 24" aria-hidden="true"><circle cx="12" cy="12" r="10"/></svg>
          velkfamilydental.com
        </li>
      </ul>
    </div>
  </section>

  <section class="card card--back" aria-label="Appointment reminder card">
    <div class="back-brand">Velk Family Dental</div>
    <div class="form">
      <div class="form__row">
        <span class="form__label">Name:</span><span class="form__dots"></span>
      </div>
      <div class="form__row">
        <span class="form__label">Date:</span><span class="form__dots"></span>
        <span class="form__label">Time:</span><span class="form__dots"></span>
        <span class="form__suffix">AM/PM</span>
      </div>
    </div>
    <p class="notice">Please give 24 hours notice cancelling your appointment or a fee may be charged</p>
  </section>
</body>
</html>
```